Retractable Banner Design for Youth Group

I would like the signage with the following as well as the following:
YOUTH VISION: Realigning the blueprint of our youth to God’s original plan.
YOUTH MISSION: Developing a generation of young people who are confident of God's irrefutable love; healing power; mercy and forgiveness; and, sovereignty.

The banner size is 33.5x 79 inches

Target Market(s)

Teenagers

Industry/Entity Type

Religious

Colors

Designer to choose colors to be used in the design.

Requirements
Must have
• Logo
• Inner Healing
• Discipleship
• Leadership Development

```html
<!DOCTYPE html>
<html lang="en">
<head>
<meta charset="utf-8">
<title>Risen Youth – Retractable Banner</title>
<link rel="stylesheet" href="https://fonts.googleapis.com/css2?family=PT+Sans:wght@400;700&family=Crimson+Text&display=swap">
<style>
  :root {
    --stage: #d9d9db;
    --paper: #ffffff;
    --brand-red: #9e1b22;
    --accent-red: #e0262c;
    --ink-grey: #4a4a4c;
    --text-light: #ffffff;
    --text-dark: #333333;
  }
  * { box-sizing: border-box; margin: 0; padding: 0; }
  html, body { width: 1200px; height: 1070px; overflow: hidden; background: var(--stage); }
  .canvas { position: relative; width: 1200px; height: 1070px; }

  .banner {
    position: absolute; left: 388px; top: 35px;
    width: 424px; height: 1000px;
    background: var(--paper);
    overflow: hidden;
    font-family: "PT Sans", Arial, sans-serif;
  }
  .banner-shapes { position: absolute; inset: 0; width: 424px; height: 1000px; }

  .brand {
    position: absolute; left: 0; right: 0; top: 78px;
    display: flex; align-items: center; justify-content: center; gap: 12px;
  }
  .brand-dot { width: 24px; height: 24px; border-radius: 50%; background: var(--brand-red); }
  .brand-name {
    font-family: "PT Sans", Arial, sans-serif; font-weight: 700;
    font-size: 34px; line-height: 40px; color: var(--brand-red);
  }
  .tagline {
    position: absolute; left: 0; right: 0; top: 124px;
    text-align: center;
    font-size: 13px; line-height: 16px; color: var(--ink-grey); letter-spacing: 1px;
  }

  .statement { position: absolute; left: 0; right: 0; text-align: center; }
  .statement-title {
    font-family: "Crimson Text", Georgia, serif; font-size: 25px; line-height: 28px;
    color: var(--accent-red); font-weight: 400;
  }
  .statement-text { color: var(--text-light); font-size: 14.5px; line-height: 20px; }
  .vision { top: 570px; }
  .vision .statement-text { margin-top: 10px; padding: 0 14px; }
  .mission { top: 653px; }
  .mission .statement-text { margin-top: 8px; padding: 0 30px; font-size: 14px; }

  .pillars {
    position: absolute; left: 0; right: 0; top: 782px;
    display: flex; justify-content: center; gap: 36px;
  }
  .pillar { width: 84px; text-align: center; color: var(--text-light); font-size: 13px; line-height: 16px; }
  .pillar-icon {
    width: 66px; height: 66px; margin: 0 auto 14px;
    border: 2px solid var(--text-light); border-radius: 50%;
    display: flex; align-items: center; justify-content: center;
  }
  .pillar-icon svg { width: 36px; height: 36px; fill: var(--accent-red); }
  .pillar.lead .pillar-label { margin-top: -6px; }

  .phone-pill {
    position: absolute; left: 91px; top: 904px; width: 238px; height: 34px;
    border-radius: 17px; background: var(--brand-red);
    display: flex; align-items: center; justify-content: center; gap: 12px;
    color: var(--text-light); font-size: 20px; letter-spacing: 0.5px;
  }
  .phone-pill svg { width: 20px; height: 20px; }

  .contact-line {
    position: absolute; left: 0; right: 0; top: 956px;
    display: flex; justify-content: center; gap: 22px;
    font-size: 14.5px; line-height: 18px; color: var(--text-dark);
  }
  .contact-item { display: flex; align-items: center; gap: 6px; }
  .contact-item::before {
    content: ""; width: 10px; height: 10px; border-radius: 50%;
    background: var(--accent-red); opacity: 0.8;
  }
</style>
</head>
<body>
<div class="canvas">
  <div class="banner">
    <svg class="banner-shapes" viewBox="0 0 424 1000">
      <defs>
        <linearGradient id="photo-tones" x1="0" y1="0" x2="1" y2="1">
          <stop offset="0" stop-color="#e7585f"/>
          <stop offset="0.35" stop-color="#c89a82"/>
          <stop offset="0.7" stop-color="#f1e6dd"/>
          <stop offset="1" stop-color="#4f9a8c"/>
        </linearGradient>
        <radialGradient id="hands-tones" cx="0.5" cy="0.5" r="0.6">
          <stop offset="0" stop-color="#d7b597"/>
          <stop offset="1" stop-color="#7c5a43"/>
        </radialGradient>
        <radialGradient id="panel-tone" cx="0.55" cy="0.45" r="0.75">
          <stop offset="0" stop-color="#5f5f62"/>
          <stop offset="1" stop-color="#262628"/>
        </radialGradient>
      </defs>

      <rect class="group-photo" x="0" y="140" width="424" height="420" fill="url(#photo-tones)"
            role="img" aria-label="Photo: group of smiling teenagers in a huddle, seen from below"/>

      <path class="header-cut" d="M0,0 H424 V136 C300,142 140,158 0,150 Z" fill="var(--paper)"/>
      <path class="header-swoosh" d="M0,148 C140,156 300,140 424,134 L424,140 C300,148 140,164 0,156 Z" fill="var(--brand-red)"/>

      <path class="photo-edge-white" d="M0,518 C140,490 300,500 424,468 L424,480 C300,512 140,502 0,530 Z" fill="var(--paper)"/>
      <path class="photo-edge-red" d="M0,530 C140,502 300,512 424,480 L424,498 C300,528 140,518 0,546 Z" fill="var(--brand-red)"/>
      <path class="info-panel" d="M0,544 C140,516 300,526 424,496 L424,940 L0,940 Z" fill="url(#panel-tone)"/>

      <circle cx="333" cy="482" r="66" fill="var(--brand-red)"/>
      <circle cx="333" cy="482" r="59" fill="var(--paper)"/>
      <circle class="hands-photo" cx="333" cy="482" r="55" fill="url(#hands-tones)"
              role="img" aria-label="Photo: many hands stacked together in a circle"/>

      <path class="footer-swoosh" d="M0,936 C150,912 280,924 424,900 L424,910 C280,934 150,922 0,946 Z" fill="var(--brand-red)"/>
      <path class="footer-cut" d="M0,946 C150,922 280,934 424,910 L424,1000 L0,1000 Z" fill="var(--paper)"/>
    </svg>

    <div class="brand">
      <span class="brand-dot"></span>
      <span class="brand-name">Risen Youth</span>
    </div>
    <div class="tagline">Rise . Grow . Lead</div>

    <section class="statement vision">
      <h2 class="statement-title">YOUTH VISION</h2>
      <p class="statement-text">Realigning the blueprint of our youth to God’s original plan.</p>
    </section>
    <section class="statement mission">
      <h2 class="statement-title">YOUTH MISSION</h2>
      <p class="statement-text">Developing a generation of young people who are confident of God’s irrefutable love; healing power; mercy and forgiveness; and, sovereignty.</p>
    </section>

    <div class="pillars">
      <div class="pillar">
        <div class="pillar-icon">
          <svg viewBox="0 0 36 36"><path d="M18 24 C10 18 7 14 7 11 a5 5 0 0 1 11 -2 a5 5 0 0 1 11 2 c0 3 -3 7 -11 13z"/><path d="M3 20 l6 8 h18 l6 -8 -2 -1 -5 5 h-16 l-5 -5z"/></svg>
        </div>
        <div class="pillar-label">Inner Healing</div>
      </div>
      <div class="pillar">
        <div class="pillar-icon">
          <svg viewBox="0 0 36 36"><circle cx="18" cy="10" r="5"/><circle cx="8" cy="14" r="4"/><circle cx="28" cy="14" r="4"/><path d="M10 30 c0 -8 3 -13 8 -13 s8 5 8 13z"/><path d="M2 30 c0 -6 2 -10 6 -10 2 0 3 1 3 1 -2 3 -2 6 -2 9z"/><path d="M34 30 c0 -6 -2 -10 -6 -10 -2 0 -3 1 -3 1 2 3 2 6 2 9z"/></svg>
        </div>
        <div class="pillar-label">Discipleship</div>
      </div>
      <div class="pillar lead">
        <div class="pillar-icon">
          <svg viewBox="0 0 36 36"><path d="M3 9 c5 -2 10 -2 14 1 v18 c-4 -3 -9 -3 -14 -1z"/><path d="M33 9 c-5 -2 -10 -2 -14 1 v18 c4 -3 9 -3 14 -1z"/></svg>
        </div>
        <div class="pillar-label">Leadership Development</div>
      </div>
    </div>

    <div class="phone-pill">
      <svg viewBox="0 0 20 20"><circle cx="10" cy="10" r="8.5" fill="none" stroke="#fff" stroke-width="1.5"/><path d="M7 5.5 l1.5 2.5 -1 1 c.6 1.4 1.6 2.4 3 3 l1 -1 2.5 1.5 -.8 1.6 c-3.6 -.2 -6.8 -3.4 -7 -7z" fill="#fff"/></svg>
      <span>555 014 2680</span>
    </div>

    <div class="contact-line">
      <span class="contact-item">hello@risenyouth.org</span>
      <span class="contact-item">www.risenyouth.org</span>
    </div>
  </div>
</div>
</body>
</html>
```